App landing page and Amber Nook template

I am building a web-based app to help people manage their lives. The app divides their life into 4 categories, Self, Relationships, Career, and Finance. I need a landing page for this application which will feature as a dashboard for each of the categories. The page will be dynamically updated as updates are received from the app. The logo will be a key feature of the page. There will be a menu to the left-hand side. A banner at the top will include interactive icons for the user to navigate the site, manage their account and logout.
I also need a template page for users to present the Ambers Nook to the end users where users can store passwords, important documents, and other important information. This template will present Secrets in either a list format or in an itemized box format.
I have attached the Application Logo for reference.

```html
<!DOCTYPE html>
<html lang="en">
<head>
<meta charset="utf-8">
<title>LifeHarbor – Your Personal Hub</title>
<link rel="stylesheet" href="https://fonts.googleapis.com/css2?family=Lexend:wght@400;500;600&family=Poppins:wght@400;500;600&display=swap">
<style>
:root{
  --blue:#145da0;
  --blue-dark:#0f4c86;
  --blue-light:#e6f2fc;
  --yellow:#f5c400;
  --yellow-soft:#fbe17a;
  --green:#1f9a4c;
  --red:#e8244f;
  --ink:#111;
  --muted:#555;
  --line:#e6e8ee;
  --head:'Lexend',sans-serif;
  --body:'Poppins',sans-serif;
}
*{box-sizing:border-box;margin:0;padding:0}
html,body{width:1200px;height:4035px;overflow:hidden}
body{font-family:var(--body);color:var(--ink);position:relative;
  background:linear-gradient(180deg,#fdeef0 0,#fff6ef 500px,#fdf3f6 1100px,#fff 1250px,#fff 100%)}
.abs{position:absolute}
.badge{position:absolute;display:inline-flex;align-items:center;gap:5px;background:#e9ebef;border-radius:20px;padding:3px 10px 3px 6px;font-size:9px;color:#333}
.badge i{width:10px;height:10px;border-radius:50%;background:var(--blue);display:inline-block;position:relative}
.badge i::after{content:"";position:absolute;left:3px;top:2px;width:3px;height:5px;border:solid #fff;border-width:0 1.3px 1.3px 0;transform:rotate(40deg)}
.badge.green i{background:var(--green)}
.badge.red i{background:var(--red)}
.underline{position:relative;display:inline-block}
.underline::after{content:"";position:absolute;right:-2%;bottom:-6px;width:52%;height:3px;border-radius:3px;background:var(--yellow)}
h1,h2,h3{font-family:var(--head);font-weight:600}

/* nav */
.nav{left:94px;top:12px;width:1011px;height:44px;background:#fff;border-radius:8px;box-shadow:0 2px 10px rgba(0,0,0,.05);display:flex;align-items:center}
.brand{position:absolute;left:22px;display:flex;align-items:center;gap:6px;font-family:var(--head);font-weight:600;font-size:13px;color:var(--blue)}
.brand span.dot{width:22px;height:22px;border-radius:50%;background:var(--blue)}
.nav ul{position:absolute;left:288px;display:flex;list-style:none;font-size:10px;color:#222}
.nav li{padding:0 12px;border-right:1px solid #ccc;line-height:10px}
.nav li:last-child{border:0}
.login{position:absolute;left:866px;font-size:10px;display:flex;align-items:center;gap:6px}
.signup{position:absolute;left:934px;background:var(--blue);color:#fff;font-size:10px;padding:7px 12px;border-radius:4px}

/* hero */
.hero-title{left:0;width:1200px;top:152px;text-align:center;font-size:57px;line-height:67px;letter-spacing:-.5px}
.hl{background:var(--yellow);border-radius:10px;padding:0 12px}
.hero-text{left:0;width:1200px;top:376px;text-align:center;font-size:11.5px;line-height:18px;color:#333}
.btn{position:absolute;font-size:11px;padding:11px 18px;border-radius:4px}
.btn.primary{left:454px;top:428px;background:var(--blue);color:#fff}
.btn.ghost{left:605px;top:428px;background:#ddd;color:#111}
.rating{left:0;width:1200px;top:484px;text-align:center;font-size:9px;color:#333}
.rating b{color:#f5b400;font-size:13px;letter-spacing:2px;margin-right:10px}
.trusted{left:937px;top:380px;font-size:9px;color:#222}
.avatars{left:937px;top:397px;display:flex;align-items:center}
.avatars i{width:22px;height:22px;border-radius:50%;border:2px solid #fff;margin-right:-6px}
.avatars small{margin-left:16px;font-size:8px;color:#444}

/* mock dashboard */
.mock{left:161px;top:525px;width:881px;height:530px;background:#fff;border-radius:16px;box-shadow:0 10px 40px rgba(20,93,160,.15);padding:4px;overflow:hidden}
.mock-inner{position:absolute;left:4px;top:4px;right:4px;bottom:4px;background:#d6ebfb;border-radius:12px}
.side{position:absolute;left:0;top:0;width:50px;height:100%;background:var(--blue);border-radius:12px 0 0 12px}
.side .av{position:absolute;left:13px;top:36px;width:26px;height:26px;border-radius:50%;background:#fbb54a;border:2px solid #fff}
.side .active{position:absolute;left:0;top:80px;width:50px;height:26px;background:#0d4a84}
.side .ic{position:absolute;left:18px;width:14px;height:14px;border:1.6px solid #cfe3f6;border-radius:4px}
.panel{position:absolute;background:#fff;border-radius:10px;font-size:8px;color:#333;padding:10px}
.panel h5{font-size:8.5px;font-weight:500;color:#1c3a5f}
.panel .sub{font-size:6px;color:#777}
.pill{position:absolute;right:10px;top:9px;font-size:6px;border:1px solid #bbb;border-radius:8px;padding:1px 8px;color:#666}

/* sections */
.sec-title{left:0;width:1200px;text-align:center;font-size:41px}
.sec-text{left:0;width:1200px;text-align:center;font-size:11px;line-height:18px;color:#333}
.cat{position:absolute;top:1330px;width:238px;height:258px;color:#fff;padding:0 24px}
.cat .icon{position:absolute;right:18px;top:28px;width:66px;height:62px;border-radius:4px}
.cat .num{position:absolute;top:92px;font-size:13px}
.cat h3{position:absolute;top:118px;font-size:18px;font-weight:500}
.cat p{position:absolute;top:150px;left:24px;right:20px;font-size:10.5px;line-height:17px}
.cat .arr{position:absolute;bottom:22px;font-size:13px}

.feat-list{left:633px;top:1858px;width:460px}
.feat-list li{list-style:none;margin-bottom:21px;font-size:13px;font-weight:500;position:relative;padding-left:12px}
.feat-list li::before{content:"";position:absolute;left:0;top:7px;width:4px;height:4px;border-radius:50%;background:var(--blue)}
.feat-list li span{display:block;font-size:10.5px;font-weight:400;color:#333;margin-top:3px}
.big-title{font-size:41px;line-height:49px}

.chartcard{position:absolute;background:#fff;border-radius:6px;box-shadow:0 8px 28px rgba(0,0,0,.08)}

.sec-card{position:absolute;top:2825px;height:234px;background:#fff;border:1px solid var(--line);box-shadow:0 4px 16px rgba(0,0,0,.04);padding:28px 28px}
.sec-card .icon{width:60px;height:56px;border-radius:3px;background:radial-gradient(circle at 50% 50%,#9fd3ad 0,#c4e6cc 40%,#e2f3e6 75%)}
.sec-card h3{font-size:23px;font-weight:500;margin-top:18px;line-height:24px}
.sec-card p{font-size:13px;line-height:22px;color:#333;margin-top:10px}

.tcard{position:absolute;top:3262px;width:293px;height:198px;background:#fff;box-shadow:0 6px 20px rgba(0,0,0,.07);padding:26px 18px}
.tcard .stars{color:#f5b400;font-size:14px;letter-spacing:1px}
.tcard .q{position:absolute;right:22px;top:10px;font-family:Georgia,serif;font-size:70px;color:#ddd;line-height:70px}
.tcard p{font-size:12.5px;line-height:19px;color:#222;margin-top:16px}
.tcard b{display:block;position:absolute;bottom:24px;left:18px;font-size:14px;font-weight:600}
.circ{position:absolute;width:50px;height:50px;border-radius:50%;display:flex;align-items:center;justify-content:center;font-size:22px}

/* footer */
.footer{left:92px;top:3545px;width:1014px;height:459px;background:var(--blue);border-radius:30px;color:#fff}
.cta{position:absolute;left:21px;top:17px;width:974px;height:133px;background:var(--yellow);border-radius:16px;overflow:hidden}
.cta::after{content:"";position:absolute;left:619px;top:-50px;width:500px;height:240px;border-radius:120px 0 0 120px;background:var(--yellow-soft)}
.cta h3{position:absolute;left:57px;top:42px;font-size:21px;font-weight:500;color:#111}
.cta p{position:absolute;left:57px;top:76px;width:470px;font-size:10.5px;line-height:17px;color:#222}
.cta .go{position:absolute;left:700px;top:54px;z-index:1;font-size:13px;font-weight:500;color:#111;display:flex;align-items:center;gap:10px}
.fcol{position:absolute;top:205px;font-size:10px;line-height:17px}
.fcol h4{font-size:13px;font-weight:500;padding-left:8px;border-left:2px solid var(--yellow);line-height:14px;margin-bottom:10px}
.fdiv{position:absolute;top:205px;width:1px;height:170px;background:rgba(255,255,255,.25)}
.nl{position:absolute;left:723px;top:332px;width:213px;height:38px;background:#fff;border-radius:20px;overflow:hidden}
.nl span{position:absolute;left:20px;top:12px;font-size:8.5px;color:#999}
.nl b{position:absolute;right:0;top:0;width:44px;height:38px;background:var(--green);border-radius:0 20px 20px 0;display:flex;align-items:center;justify-content:center;font-size:16px}
.soc{position:absolute;top:384px;width:20px;height:20px;border-radius:50%;background:#fff}
</style>
</head>
<body>

<!-- navigation -->
<nav class="abs nav">
  <div class="brand"><span class="dot"></span>LifeHarbor</div>
  <ul><li>Self</li><li>Relationships</li><li>Career</li><li>FinanceEatures</li><li>Ambers Nook</li><li>Contact Us</li></ul>
  <div class="login"><svg width="11" height="11" viewBox="0 0 12 12"><circle cx="6" cy="4" r="2.6" fill="none" stroke="#222" stroke-width="1.2"/><path d="M1.5 11.5c0-2.6 2-4 4.5-4s4.5 1.4 4.5 4" fill="none" stroke="#222" stroke-width="1.2"/></svg>Login</div>
  <div class="signup">Sign Up</div>
</nav>

<!-- hero -->
<span class="badge green" style="left:492px;top:133px"><i></i>Manage Your Lives</span>
<span class="badge green" style="left:604px;top:133px"><i></i>Your Ambers Nook</span>
<h1 class="abs hero-title">Your Personal Hub<br>for Self, Relationships,<br>Career, <span class="hl">and Finance</span></h1>
<p class="abs hero-text">Our app is designed to help you balance and optimize four key areas: Self, Relationships, Career, and Finance.<br>Stay organized, stay focused, and achieve your goals with LifeHarbor.</p>
<div class="btn primary">Get Started for Free</div>
<div class="btn ghost">Request a Demo</div>
<div class="abs rating"><b>★★★★★</b>Based on 10K+ reviews</div>
<div class="abs trusted">Client Trusted</div>
<div class="abs avatars" role="img" aria-label="Small portraits of trusted clients">
  <i style="background:#8b6a55"></i><i style="background:#6b7d90"></i><i style="background:#a07a63"></i><i style="background:#4d5662"></i>
  <small><span style="color:#f5b400">★</span> 1,234+</small>
</div>

<!-- dashboard preview -->
<div class="abs mock">
 <div class="mock-inner">
  <div class="side">
    <div class="av"></div><div class="active"></div>
    <div class="ic" style="top:86px;border-color:#fff"></div>
    <div class="ic" style="top:120px"></div><div class="ic" style="top:153px"></div>
    <div class="ic" style="top:186px;border-radius:50%"></div><div class="ic" style="top:219px;border:0;border-top:1.6px solid #cfe3f6;border-bottom:1.6px solid #cfe3f6;height:10px"></div>
    <div class="ic" style="top:496px"></div>
  </div>

  <div class="panel" style="left:70px;top:7px;width:183px;height:190px">
    <h5>Lorem ipsum</h5><span class="pill">Week</span>
    <div style="margin:18px 0 0 45px;font-size:18px;color:#1c3a5f"><span style="color:var(--blue)">↑</span>1974</div>
    <div class="sub" style="text-align:center;margin-top:2px">Dolor sit amet, consectetuer<br>adipiscing elit</div>
    <div style="margin:24px 0 0 45px;font-size:18px;color:#1c3a5f"><span style="color:#f0a020">↓</span> 287</div>
    <div class="sub" style="text-align:center;margin-top:2px">Vel illum dolore eu feugiat<br>nulla facilisis at vero</div>
  </div>

  <div class="panel" style="left:270px;top:7px;width:185px;height:190px;text-align:center">
    <h5 style="color:#333">‹ &nbsp;January&nbsp; ›</h5>
    <svg width="165" height="150" viewBox="0 0 165 150" font-size="7" fill="#333" font-family="Poppins">
      <g fill="#666"><text x="4" y="14">sun</text><text x="27" y="14">mon</text><text x="52" y="14">tue</text><text x="74" y="14">wed</text><text x="98" y="14">thu</text><text x="124" y="14">fri</text><text x="147" y="14">sat</text></g>
      <text x="128" y="35">1</text><text x="150" y="35">2</text>
      <text x="8" y="56">3</text><text x="32" y="56">4</text><text x="56" y="56">5</text><text x="80" y="56">6</text><text x="103" y="56">7</text><text x="128" y="56">8</text><text x="150" y="56">9</text>
      <text x="6" y="77">10</text><text x="30" y="77">11</text><text x="54" y="77">12</text><text x="78" y="77">13</text><circle cx="105" cy="74" r="7" fill="none" stroke="#c9a21a"/><text x="101" y="77">14</text><text x="126" y="77">15</text><text x="148" y="77">16</text>
      <text x="6" y="98">17</text><text x="30" y="98">18</text><text x="54" y="98">19</text><text x="78" y="98">20</text><text x="101" y="98">21</text><text x="126" y="98">22</text><text x="148" y="98">23</text>
      <text x="6" y="119">24</text><circle cx="34" cy="116" r="7" fill="none" stroke="#1f9a4c"/><text x="30" y="119">25</text><text x="54" y="119">26</text><text x="78" y="119">27</text><circle cx="105" cy="116" r="7" fill="none" stroke="#c9a21a"/><text x="101" y="119">28</text><text x="126" y="119">29</text><text x="148" y="119">30</text>
      <text x="6" y="140">31</text>
    </svg>
  </div>

  <div class="panel" style="left:470px;top:7px;width:184px;height:115px">
    <h5>Lorem ipsum</h5>
    <svg width="164" height="80" viewBox="0 0 164 80"><rect x="2" y="8" width="150" height="4" rx="2" fill="#dce8f4"/><rect x="2" y="8" width="102" height="4" rx="2" fill="#2d7fd0"/><text x="2" y="22" font-size="6" fill="#777">Consectetuer</text>
    <rect x="2" y="32" width="150" height="4" rx="2" fill="#dce8f4"/><rect x="2" y="32" width="150" height="4" rx="2" fill="#f0a020"/><text x="2" y="46" font-size="6" fill="#777">Adipiscing</text>
    <rect x="2" y="56" width="150" height="4" rx="2" fill="#dce8f4"/><rect x="2" y="56" width="112" height="4" rx="2" fill="#2d7fd0"/><text x="2" y="70" font-size="6" fill="#777">Sit amet</text></svg>
  </div>

  <div class="panel" style="left:470px;top:137px;width:184px;height:231px;text-align:center">
    <h5 style="text-align:left">Lorem ipsum</h5><div class="sub" style="text-align:left">Duis autem vel eum iriure</div>
    <svg width="110" height="110" viewBox="0 0 110 110" style="margin-top:6px"><circle cx="55" cy="55" r="46" fill="none" stroke="#e3eef9" stroke-width="6"/><path d="M55 9a46 46 0 1 1-46 46" fill="none" stroke="#2d7fd0" stroke-width="6" stroke-linecap="round"/><text x="55" y="63" text-anchor="middle" font-size="24" fill="#1c3a5f" font-family="Poppins">75%</text></svg>
    <div class="sub" style="margin-top:4px">Lorem ipsum dolor sit amet,<br>consectetuer adipiscing</div>
    <div style="margin:8px auto 0;width:122px;background:var(--blue);color:#fff;border-radius:10px;font-size:7px;padding:4px">Suscipit</div>
  </div>

  <div class="panel" style="left:627px;top:7px;width:185px;height:31px;padding:8px 14px;color:#888">Search...
    <span style="position:absolute;right:6px;top:6px;width:19px;height:19px;border-radius:50%;background:var(--blue)"></span></div>

  <div class="panel" style="left:627px;top:54px;width:185px;height:188px">
    <h5>Commodo</h5><div class="sub">Sed diam nonummy nibh euismod</div>
    <svg width="165" height="145" viewBox="0 0 165 145"><path d="M2 60 L15 30 L28 50 L40 22 L54 48 L68 28 L82 52 L96 20 L110 45 L124 25 L140 50 L160 30 L160 66 L2 66Z" fill="#aed3f3"/><path d="M2 60 L15 30 L28 50 L40 22 L54 48 L68 28 L82 52 L96 20 L110 45 L124 25 L140 50 L160 30" fill="none" stroke="#2d7fd0" stroke-width="1.4"/>
    <path d="M2 140 L2 110 L15 96 L28 115 L40 92 L54 112 L68 94 L82 116 L96 90 L110 112 L124 98 L140 114 L160 96 L160 140Z" fill="#f6d27a"/><path d="M2 110 L15 96 L28 115 L40 92 L54 112 L68 94 L82 116 L96 90 L110 112 L124 98 L140 114 L160 96" fill="none" stroke="#e59a12" stroke-width="1.4"/></svg>
  </div>

  <div class="panel" style="left:627px;top:259px;width:185px;height:69px">
    <h5>Delenit augue</h5>
    <svg width="165" height="30" viewBox="0 0 165 30"><rect x="2" y="6" width="105" height="6" rx="3" fill="#2d7fd0"/><rect x="107" y="6" width="55" height="6" rx="3" fill="#f0a020"/><g font-size="5.5" fill="#777"><circle cx="6" cy="24" r="2" fill="#2d7fd0"/><text x="11" y="26">Lorem</text><circle cx="58" cy="24" r="2" fill="#7fb7ea"/><text x="63" y="26">Ipsum</text><circle cx="110" cy="24" r="2" fill="#f0a020"/><text x="115" y="26">Dolor</text></g></svg>
  </div>

  <div class="panel" style="left:627px;top:345px;width:185px;height:168px">
    <h5>Consectetuer</h5><span class="pill">Month</span>
    <svg width="165" height="130" viewBox="0 0 165 130"><circle cx="78" cy="68" r="48" fill="none" stroke="#f0a020" stroke-width="12"/><path d="M78 20a48 48 0 0 1 45 62" fill="none" stroke="#2d7fd0" stroke-width="12"/><text x="92" y="60" font-size="12" fill="#2d7fd0" font-family="Poppins">30%</text><text x="96" y="68" font-size="5" fill="#777">Lorem</text><text x="46" y="82" font-size="12" fill="#f0a020" font-family="Poppins">70%</text><text x="54" y="90" font-size="5" fill="#777">Ipsum</text></svg>
  </div>

  <div class="panel" style="left:70px;top:215px;width:385px;height:153px">
    <h5>Dolor sit amet</h5><span class="pill">All time</span>
    <svg width="365" height="120" viewBox="0 0 365 120"><g stroke="#eee"><line x1="20" y1="15" x2="360" y2="15"/><line x1="20" y1="45" x2="360" y2="45"/><line x1="20" y1="75" x2="360" y2="75"/><line x1="20" y1="100" x2="360" y2="100"/></g>
    <path d="M30 70 C60 20 90 40 110 70 S160 110 190 70 S240 40 270 80 S320 40 350 60" fill="none" stroke="#2d7fd0" stroke-width="1.6"/>
    <path d="M30 50 C60 80 100 90 130 50 S190 20 220 60 S260 20 280 30 S320 90 350 80" fill="none" stroke="#f0a020" stroke-width="1.6"/>
    <g font-size="6" fill="#777"><line x1="70" y1="112" x2="90" y2="112" stroke="#2d7fd0" stroke-width="2"/><text x="96" y="114">Lorem</text><line x1="180" y1="112" x2="200" y2="112" stroke="#f0a020" stroke-width="2"/><text x="206" y="114">Ipsum</text></g></svg>
  </div>

  <div class="panel" style="left:70px;top:386px;width:282px;height:127px">
    <svg width="262" height="110" viewBox="0 0 262 110"><g font-size="5" fill="#777"><text x="0" y="18">OCT</text><text x="0" y="38">NOV</text><text x="0" y="58">DEC</text><text x="0" y="78">JAN</text></g>
    <rect x="20" y="12" width="40" height="8" fill="#2d7fd0"/><rect x="60" y="12" width="50" height="8" fill="#7fb7ea"/><rect x="110" y="12" width="40" height="8" fill="#a9cff2"/><rect x="150" y="12" width="55" height="8" fill="#145da0"/>
    <rect x="20" y="32" width="30" height="8" fill="#7fb7ea"/><rect x="50" y="32" width="40" height="8" fill="#145da0"/><rect x="90" y="32" width="35" height="8" fill="#2d7fd0"/>
    <rect x="20" y="52" width="60" height="8" fill="#145da0"/><rect x="80" y="52" width="30" height="8" fill="#2d7fd0"/><rect x="110" y="52" width="40" height="8" fill="#a9cff2"/><rect x="150" y="52" width="40" height="8" fill="#7fb7ea"/>
    <rect x="20" y="72" width="90" height="8" fill="#2d7fd0"/><rect x="110" y="72" width="35" height="8" fill="#7fb7ea"/><rect x="145" y="72" width="25" height="8" fill="#a9cff2"/>
    <g font-size="5" fill="#777"><rect x="40" y="98" width="5" height="5" fill="#7fb7ea"/><text x="48" y="103">Lorem</text><rect x="90" y="98" width="5" height="5" fill="#2d7fd0"/><text x="98" y="103">Ipsum</text><rect x="140" y="98" width="5" height="5" fill="#145da0"/><text x="148" y="103">Dolor</text><rect x="190" y="98" width="5" height="5" fill="#145da0"/><text x="198" y="103">Nonummy</text></g></svg>
  </div>

  <div class="panel" style="left:369px;top:386px;width:285px;height:127px">
    <h5>Adipiscing</h5>
    <svg width="265" height="95" viewBox="0 0 265 95"><g fill="#e3b340"><rect x="20" y="40" width="5" height="40"/><rect x="52" y="30" width="5" height="50"/><rect x="84" y="50" width="5" height="30"/><rect x="116" y="25" width="5" height="55"/><rect x="148" y="45" width="5" height="35"/><rect x="180" y="35" width="5" height="45"/><rect x="212" y="20" width="5" height="60"/><rect x="244" y="45" width="5" height="35"/></g>
    <g fill="#f4d98a"><rect x="27" y="55" width="5" height="25"/><rect x="59" y="50" width="5" height="30"/><rect x="91" y="35" width="5" height="45"/><rect x="123" y="55" width="5" height="25"/><rect x="155" y="30" width="5" height="50"/><rect x="187" y="55" width="5" height="25"/><rect x="219" y="50" width="5" height="30"/><rect x="251" y="60" width="5" height="20"/></g>
    <g font-size="5" fill="#777"><text x="18" y="91">Sun</text><text x="52" y="91">Mon</text><text x="86" y="91">Tue</text><text x="116" y="91">Wed</text><text x="150" y="91">Thu</text><text x="184" y="91">Fri</text><text x="214" y="91">Sat</text></g></svg>
  </div>
 </div>
</div>

<!-- personal dashboard -->
<span class="badge" style="left:535px;top:1169px"><i></i>Dashboard Overview</span>
<h2 class="abs sec-title" style="top:1196px"><span class="underline">Your Personal Dashboard</span></h2>
<p class="abs sec-text" style="top:1268px">Get a comprehensive overview of your life in one place. Your dashboard dynamically updates with<br>real-time data, giving you insights and reminders for each category.</p>

<div class="cat" style="left:94px;background:var(--green)"><div class="icon" role="img" aria-label="Icon illustration of a personal planner screen" style="background:radial-gradient(circle,#7cc595 0,#b9e1c6 45%,#eef8f1 80%)"></div><span class="num">01</span><h3>Self</h3><p>Track your health, hobbies, and personal development.</p><span class="arr">→</span></div>
<div class="cat" style="left:349px;background:var(--blue)"><div class="icon" role="img" aria-label="Icon illustration of a handshake" style="background:radial-gradient(circle,#6fa3d4 0,#b5d2ee 45%,#eef5fc 80%)"></div><span class="num">02</span><h3>Relationships</h3><p>Keep tabs on important dates, communication, &amp; relationship goals.</p><span class="arr">→</span><span class="arr" style="left:150px">→</span></div>
<div class="cat" style="left:606px;background:var(--yellow)"><div class="icon" role="img" aria-label="Icon illustration of a person climbing career steps" style="background:radial-gradient(circle,#f3cf47 0,#f8e48f 45%,#fdf6d8 80%)"></div><span class="num" style="color:#fff4c2">03</span><h3>Career</h3><p style="color:#fff4c2">Monitor your professional progress, projects, and career aspirations.</p><span class="arr">→</span></div>
<div class="cat" style="left:868px;background:var(--red)"><div class="icon" role="img" aria-label="Icon illustration of a hand holding a coin" style="background:radial-gradient(circle,#ef7d96 0,#f6bccb 45%,#fdeef2 80%)"></div><span class="num">04</span><h3>Finance</h3><p>Manage your budget, savings, and financial goals.</p></div>

<!-- features -->
<div class="abs" style="left:149px;top:1686px;width:439px;height:461px;background:linear-gradient(180deg,#fde1e6,#fdf1f3 70%,#fff);border-radius:10px 10px 0 0"></div>
<div class="abs" style="left:227px;top:1760px;width:270px;height:60px;background:#fbc7d2;border-radius:8px"></div>
<div class="chartcard" style="left:200px;top:1816px;width:322px;height:276px">
  <div style="position:absolute;left:22px;top:32px;font-size:15px">Follower Growth</div>
  <svg class="abs" style="left:16px;top:70px" width="296" height="200" viewBox="0 0 296 200">
    <g font-size="8" fill="#888" font-family="Poppins"><text x="6" y="14">8K</text><text x="6" y="46">6K</text><text x="6" y="78">4K</text><text x="6" y="110">2K</text><text x="6" y="142">1K</text>
    <text x="28" y="176">2/8</text><text x="86" y="176">3/8</text><text x="144" y="176">4/8</text><text x="202" y="176">5/8</text><text x="262" y="176">6/8</text></g>
    <path d="M32 124 C60 90 80 120 110 110 S140 70 150 80 S180 130 200 120 S250 80 270 50" fill="none" stroke="#f4b8c6" stroke-width="6" stroke-linecap="round"/>
    <path d="M32 124 C60 90 80 120 110 110 S140 70 150 80 S180 130 200 120" fill="none" stroke="#c9304f" stroke-width="3" stroke-linecap="round"/>
    <line x1="150" y1="60" x2="150" y2="80" stroke="#e8244f" stroke-dasharray="2 2"/>
    <rect x="130" y="22" width="44" height="40" rx="5" fill="#e8244f"/><text x="152" y="42" text-anchor="middle" fill="#fff" font-size="11" font-family="Poppins">5.3K</text><text x="152" y="54" text-anchor="middle" fill="#fff" font-size="7" font-family="Poppins">Follower</text>
  </svg>
</div>

<span class="badge" style="left:628px;top:1700px"><i></i>Key Features</span>
<h2 class="abs big-title" style="left:633px;top:1726px">Top Features to<br><span class="underline">Enhance Your Life</span></h2>
<ul class="abs feat-list">
  <li>Personalized Insights<span>Receive tailored advice and reminders.</span></li>
  <li>Interactive Charts<span>Visualize your progress with easy-to-read charts and graphs.</span></li>
  <li>Task Management<span>Stay on top of your to-do lists and deadlines.</span></li>
  <li>Secure Storage<span>Safely store important documents and passwords in your Ambers Nook.</span></li>
</ul>

<!-- nook -->
<span class="badge red" style="left:160px;top:2188px"><i></i>Ambers Nook</span>
<h2 class="abs big-title" style="left:167px;top:2215px">Your Secure<br><span class="underline">Ambers Nook</span></h2>
<div class="abs" style="left:167px;top:2328px;width:400px;font-size:10.5px;line-height:17px;color:#222">
  <p>Store and manage your most important information securely.<br>The Ambers Nook is designed to keep your passwords, documents, and vital information safe and easily accessible.</p>
  <p style="font-size:14px;color:#888;margin-top:4px">Add New Secrets</p>
  <p style="margin-top:3px">Easily add new passwords, documents, or other important information with our simple form.</p>
</div>
<ul class="abs feat-list" style="left:167px;top:2458px;width:400px">
  <li>Passwords<span>Store and manage your passwords securely.</span></li>
  <li>Documents<span>Upload and access important documents anytime, anywhere.</span></li>
  <li>Notes<span>Keep important notes and reminders safe.</span></li>
</ul>

<div class="abs" style="left:644px;top:2191px;width:422px;height:426px;background:linear-gradient(180deg,#d9ecfb,#eef6fd);border-radius:10px"></div>
<div class="abs" style="left:719px;top:2264px;width:271px;height:72px;background:#b9dcf8;border-radius:8px"></div>
<div class="chartcard" style="left:685px;top:2330px;width:338px;height:263px">
  <span style="position:absolute;left:18px;top:22px;width:20px;height:20px;border-radius:50%;background:#e3eef9"></span>
  <div style="position:absolute;left:50px;top:24px;font-size:12px;color:var(--blue)">Conversion rate</div>
  <div style="position:absolute;left:188px;top:16px;font-size:22px;font-weight:600;color:var(--blue)">↗ 12.32%</div>
  <div style="position:absolute;left:220px;top:46px;font-size:7px;color:#2d7fd0">Last month avg rate</div>
  <svg class="abs" style="left:12px;top:70px" width="315" height="180" viewBox="0 0 315 180">
    <defs><linearGradient id="barGrad" x1="0" y1="0" x2="0" y2="1"><stop offset="0" stop-color="#2d7fd0"/><stop offset="1" stop-color="#d6eafb"/></linearGradient></defs>
    <g font-size="6" fill="#888" font-family="Poppins"><text x="4" y="14">20</text><text x="4" y="36">16</text><text x="4" y="58">12</text><text x="4" y="80">8</text><text x="4" y="102">4</text><text x="4" y="124">0</text></g>
    <g fill="url(#barGrad)">
      <rect x="24" y="20" width="10" height="108" rx="5"/><rect x="46" y="80" width="10" height="48" rx="5"/><rect x="68" y="70" width="10" height="58" rx="5"/><rect x="90" y="55" width="10" height="73" rx="5"/><rect x="112" y="40" width="10" height="88" rx="5"/><rect x="134" y="85" width="10" height="43" rx="5"/><rect x="156" y="30" width="10" height="98" rx="5"/><rect x="178" y="18" width="10" height="110" rx="5"/><rect x="200" y="90" width="10" height="38" rx="5"/><rect x="222" y="50" width="10" height="78" rx="5"/><rect x="244" y="78" width="10" height="50" rx="5"/><rect x="266" y="34" width="10" height="94" rx="5"/><rect x="288" y="92" width="10" height="36" rx="5"/>
    </g>
    <g font-size="6" fill="#888" font-family="Poppins"><text x="22" y="145">2/8</text><text x="44" y="145">3/8</text><text x="66" y="145">4/8</text><text x="88" y="145">5/8</text><text x="110" y="145">6/8</text><text x="132" y="145">7/8</text><text x="154" y="145">8/8</text><text x="176" y="145">9/8</text><text x="196" y="145">10/8</text><text x="218" y="145">11/8</text><text x="240" y="145">12/8</text><text x="262" y="145">13/8</text><text x="284" y="145">14/8</text></g>
  </svg>
</div>

<!-- security -->
<span class="badge" style="left:546px;top:2676px"><i></i>Security Features</span>
<h2 class="abs sec-title" style="top:2700px"><span class="underline">Top-Notch Security</span></h2>
<p class="abs sec-text" style="top:2770px">Your privacy is our priority. LifeHarbor uses advanced encryption to ensure your data is protected.</p>
<div class="sec-card" style="left:128px;width:294px"><div class="icon" role="img" aria-label="Icon illustration of an encrypted data chip"></div><h3>Encryption</h3><p>All data is encrypted for<br>maximum security.</p></div>
<div class="sec-card" style="left:453px;width:291px"><div class="icon" role="img" aria-label="Icon illustration of a phone with a verification code"></div><h3>Two-Factor<br>Authentication</h3><p>Add an extra layer of protection<br>to your account.</p></div>
<div class="sec-card" style="left:779px;width:293px"><div class="icon" role="img" aria-label="Icon illustration of connected user access nodes"></div><h3>Access Controls</h3><p>Manage who can access your<br>secrets.</p></div>

<!-- testimonials -->
<span class="badge red" style="left:145px;top:3135px"><i></i>User Testimonials</span>
<h2 class="abs big-title" style="left:151px;top:3162px"><span class="underline">What Our Users Say</span></h2>
<div class="circ" style="left:941px;top:3166px;background:#e4e4e4;color:#222">←</div>
<div class="circ" style="left:996px;top:3166px;background:var(--blue);color:#fff">→</div>
<div class="tcard" style="left:132px"><span class="stars">★★★★★</span><span class="q">“</span><p>“LifeHarbor has transformed the way I manage my life. The dashboard is incredibly intuitive and helps me stay on top of everything.”</p><b>- Maris Colte</b></div>
<div class="tcard" style="left:453px"><span class="stars">★★★★★</span><span class="q">“</span><p>"Having all my important information in one secure place gives me peace of mind. The Ambers Nook is a game-changer!"</p><b>- Tessa Wren</b></div>
<div class="tcard" style="left:784px"><span class="stars">★★★★★</span><span class="q">“</span><p>“LifeHarbor has transformed the way I manage my life. The dashboard is incredibly intuitive and helps me stay on top of everything.”</p><b>- Ilona Park</b></div>

<!-- footer -->
<footer class="abs footer">
  <div class="cta">
    <h3>Get Started Today!</h3>
    <p>Ready to take control of your life? Sign up now and start using LifeHarbor to organize, manage, and optimize every aspect of your life.</p>
    <div class="go">Contact Us Now <svg width="36" height="12" viewBox="0 0 36 12"><path d="M0 6h34M28 1l6 5-6 5" fill="none" stroke="#111" stroke-width="1.4"/></svg></div>
  </div>
  <div class="fcol" style="left:62px;top:200px;width:170px">
    <div style="display:flex;align-items:center;gap:8px;font-family:var(--head);font-weight:600;font-size:13px"><span style="width:34px;height:34px;border-radius:50%;background:#fff;display:inline-block"></span>LifeHarbor</div>
    <p style="margin-top:26px;line-height:17px">Our app is designed to help you balance and optimize four key areas: Self, Relationships, Career, and Finance.</p>
  </div>
  <div class="fdiv" style="left:250px"></div>
  <div class="fcol" style="left:286px"><h4>Quick Links</h4><div style="padding-left:2px;line-height:18.5px">Self<br>Relationships<br>Career<br>Finance<br>Eatures<br>Ambers Nook<br>Contact Us</div></div>
  <div class="fdiv" style="left:445px"></div>
  <div class="fcol" style="left:493px"><h4>Contact Us</h4>
    <div style="margin-top:14px">☏ &nbsp;+1(555)-014-2290</div>
    <div style="margin-top:13px;text-decoration:underline">✉ &nbsp;hello@lifeharbor.app</div>
    <div style="margin-top:13px;padding-left:20px;text-indent:-20px">⌖ &nbsp;&nbsp;Registered office: 18 Alder Row,<br>Tallinn</div>
  </div>
  <div class="fdiv" style="left:672px"></div>
  <div class="fcol" style="left:723px;width:220px"><h4>Subscribe Newsletter</h4><p style="line-height:15px">Subscribe newsletter for the latest<br>offers and news</p></div>
  <div class="nl"><span>Enter Email...</span><b>→</b></div>
  <span class="soc" style="left:735px"></span><span class="soc" style="left:765px"></span><span class="soc" style="left:795px"></span><span class="soc" style="left:825px"></span>
  <div style="position:absolute;left:60px;top:422px;font-size:8.5px">Copyrights 2024. All Rights Reserved</div>
  <div style="position:absolute;right:56px;top:422px;font-size:8.5px">Privacy Policy | Terms &amp; Conditions</div>
</footer>

</body>
</html>
```